Reworking our Ayurvedic Tea Boxes with Mordern and New look.

We are a Tea Wholesale company for retailers and health food stores. We have currently a Ayurvedic wellness tea line needs an updated packaging. We would like to see new modern, clean and beautiful new fresh look. Our current packaging can be seen at http://leafmerchantco.example/c/7720815/1/herbal-blends.html

We are going to launch various categories in the loose leaf tea line. This is just the first step. At present 9 different exsit in the wellnes line.
Updates

Target Market(s)

Health Food Stores, Specialty Food Stores, Grocery Stores.

Industry/Entity Type

It Company

Requirements
Must have
• - Name of the of the tea type should be clearly visible.
• - A modern fresh look. Not to heavy with design work.
Nice to have
• Box size is 8 cm (L) X 4.5 cm (W) X 15cm (H)

```html
<!DOCTYPE html>
<html lang="en">
<head>
<meta charset="UTF-8">
<title>Verdant Cup – Ayurvedic Tea Boxes</title>
<link href="https://fonts.googleapis.com/css2?family=Didact+Gothic&family=Nunito:wght@300;400&family=Open+Sans:wght@400&display=swap" rel="stylesheet">
<style>
  :root {
    --page-bg: #ffffff;
    --box-white: #ffffff;
    --box-edge: #dcdcdc;
    --brand-ink: #2b2b2b;
    --arc-green: #8cc751;
    --open-air-green: #7dc243;
    --winter-blue: #24399a;
    --label-white: #ffffff;
    --tea-dark: #5a4a2a;
    --tea-mid: #8a6a34;
    --tea-light: #b98a3e;
  }
  * { margin: 0; padding: 0; box-sizing: border-box; }
  html, body {
    width: 1200px; height: 1043px; overflow: hidden;
    background: var(--page-bg);
  }
  .canvas { position: relative; width: 1200px; height: 1043px; }

  .tea-box {
    position: absolute;
    width: 510px; height: 956px;
    background: var(--box-white);
    border: 1px solid var(--box-edge);
    box-shadow: 0 14px 10px -8px rgba(0,0,0,0.45);
    overflow: hidden;
  }
  .tea-box--open-air { left: 35px; top: 27px; --band: var(--open-air-green); }
  .tea-box--winter { left: 597px; top: 24px; height: 959px; --band: var(--winter-blue); }

  .brand-name {
    position: absolute; left: 0; right: 0; top: 180px;
    text-align: center;
    font-family: "Didact Gothic", sans-serif;
    font-size: 42px; letter-spacing: 2px;
    color: var(--brand-ink);
  }

  .color-band {
    position: absolute; left: 0; right: 0; top: 521px; bottom: 0;
    background: var(--band);
  }

  .line-arc { position: absolute; left: 0; top: 0; width: 510px; height: 520px; }
  .line-arc text {
    font-family: "Nunito", sans-serif; font-weight: 400;
    font-size: 30px; letter-spacing: 1.5px; fill: var(--arc-green);
  }

  .leaf-sample {
    position: absolute; left: 135px; top: 386px;
    width: 240px; height: 240px; border-radius: 50%;
    background: radial-gradient(circle at 40% 40%, var(--tea-light) 0%, var(--tea-mid) 45%, var(--tea-dark) 100%);
  }

  .blend-name {
    position: absolute; left: 0; right: 0; top: 756px;
    text-align: center;
    font-family: "Nunito", sans-serif; font-weight: 300;
    font-size: 38px; color: var(--label-white);
  }
  .net-weight {
    position: absolute; left: 0; right: 0; top: 900px;
    text-align: center;
    font-family: "Open Sans", sans-serif;
    font-size: 21px; color: var(--label-white);
  }
</style>
</head>
<body>
<main class="canvas">

  <section class="tea-box tea-box--open-air">
    <div class="color-band"></div>
    <div class="brand-name">Verdant Cup</div>
    <svg class="line-arc" viewBox="0 0 510 520" aria-hidden="true">
      <path id="arc-open-air" d="M 117 506 A 140 140 0 0 1 397 506" fill="none"/>
      <text><textPath href="#arc-open-air" startOffset="50%" text-anchor="middle">Ayurvedic Tea</textPath></text>
    </svg>
    <div class="leaf-sample" role="img" aria-label="Photo of loose leaf herbal tea blend"></div>
    <div class="blend-name">Open Air Tea</div>
    <div class="net-weight">NET WEIGHT 3.5oz</div>
  </section>

  <section class="tea-box tea-box--winter">
    <div class="color-band" style="top:524px"></div>
    <div class="brand-name" style="top:183px">Verdant Cup</div>
    <svg class="line-arc" viewBox="0 0 510 520" aria-hidden="true" style="top:3px">
      <path id="arc-winter" d="M 117 506 A 140 140 0 0 1 397 506" fill="none"/>
      <text><textPath href="#arc-winter" startOffset="50%" text-anchor="middle">Ayurvedic Tea</textPath></text>
    </svg>
    <div class="leaf-sample" style="top:389px" role="img" aria-label="Photo of loose leaf herbal tea blend"></div>
    <div class="blend-name" style="top:759px">Winter Ease</div>
    <div class="net-weight" style="top:903px">NET WEIGHT 3.5oz</div>
  </section>

</main>
</body>
</html>
```